The most modern business card ever !!!

Our company call “Vantilo”. Vantilo is a technology company specialized in cruises solutions. Out main product is a platform to reserve cruises. This is a revolutionary platform that make easier to travel agencies and final users to reserve cruises across dozen companies like tarvik, welbi, dpv, hbt, etc..We are a “start up”, with a young team of developers and we want to transmit it.. For it, we want something different, a modern business card that represent cruises and technology.. When someone receive this card, this person should say: wowww this is different… this is modern… this is a cruise related company..
Contact Information for Business Card
Requirements
Must have
- diferent, modern
Should not have
- traditions business card

```html
<!DOCTYPE html>
<html lang="en">
<head>
<meta charset="utf-8">
<title>Vantilo – Business Card</title>
<link href="https://fonts.googleapis.com/css2?family=Exo+2:wght@300;400;500;600&display=swap" rel="stylesheet">
<style>
  :root {
    --backdrop: #3b3835;
    --card-light: #b9b9b7;
    --card-mid: #a3a3a1;
    --card-edge: #d6d6d4;
    --ink: #1b2126;
    --accent: #1f7f95;
    --icon-fill: #1e2226;
    --icon-line: #d9d9d7;
    --hull: #1a1c1e;
    --url: #d8c9a8;
  }
  * { margin: 0; padding: 0; box-sizing: border-box; }
  html, body { width: 1200px; height: 1152px; overflow: hidden; }
  body {
    background: var(--backdrop);
    font-family: "Exo 2", sans-serif;
    color: var(--ink);
    position: relative;
  }
  .card {
    position: absolute;
    left: 300px; top: 51px;
    width: 600px; height: 1050px;
    border-radius: 26px;
    border: 2px solid var(--card-edge);
    background: linear-gradient(170deg, var(--card-light) 0%, var(--card-mid) 55%, #9c9c9a 100%);
    overflow: hidden;
  }
  .brand-name {
    position: absolute;
    top: 44px; left: 0; width: 100%;
    text-align: center;
    font-size: 104px;
    font-weight: 500;
    letter-spacing: 2px;
    color: var(--ink);
    line-height: 1;
  }
  .profile-ring {
    position: absolute;
    left: 263px; top: 218px;
    width: 72px; height: 72px;
    border: 3px solid var(--accent);
    border-radius: 50%;
  }
  .name-rule {
    position: absolute;
    top: 341px; height: 2px;
    background: var(--ink);
  }
  .name-rule.left { left: 0; width: 99px; }
  .name-rule.right { left: 502px; width: 98px; }
  .name-bar {
    position: absolute;
    top: 298px; width: 2px; height: 87px;
    background: var(--ink);
  }
  .name-bar.left { left: 99px; }
  .name-bar.right { left: 500px; }
  .person-name {
    position: absolute;
    top: 302px; left: 101px; width: 399px;
    text-align: center;
    font-size: 47px; font-weight: 500;
    letter-spacing: 1.5px;
    line-height: 1;
  }
  .person-role {
    position: absolute;
    top: 352px; left: 101px; width: 399px;
    text-align: center;
    font-size: 29px; font-weight: 300;
    letter-spacing: 0.5px;
    line-height: 1;
  }
  .contact-list { list-style: none; }
  .contact-item {
    position: absolute;
    left: 110px;
    display: flex; align-items: center;
  }
  .contact-icon {
    width: 52px; height: 52px;
    border-radius: 7px;
    background: var(--icon-fill);
    display: flex; align-items: center; justify-content: center;
    flex-shrink: 0;
  }
  .contact-text {
    margin-left: 19px;
    font-size: 33px; font-weight: 400;
    letter-spacing: 2px;
    line-height: 1.05;
  }
  .contact-text.email { font-size: 32px; letter-spacing: 0.5px; }
  .contact-text.address { font-size: 30px; letter-spacing: 0.3px; line-height: 1.1; }
  .item-mobile { top: 514px; }
  .item-office { top: 574px; }
  .item-email { top: 632px; }
  .item-address { top: 694px; }
  .ship-artwork {
    position: absolute;
    left: 0; bottom: 0;
    width: 600px; height: 230px;
    background: linear-gradient(165deg, rgba(26,28,30,0) 0%, rgba(26,28,30,0.55) 35%, var(--hull) 75%);
  }
  .web-address {
    position: absolute;
    left: 230px; top: 992px;
    font-size: 21px; font-weight: 400;
    letter-spacing: 0.5px;
    color: var(--url);
  }
</style>
</head>
<body>
  <main class="card">
    <h1 class="brand-name">Vantilo</h1>

    <div class="profile-ring" aria-hidden="true"></div>

    <div class="name-rule left"></div>
    <div class="name-bar left"></div>
    <p class="person-name">Elan Roswell</p>
    <p class="person-role">SALES REPRESENTATIVE</p>
    <div class="name-bar right"></div>
    <div class="name-rule right"></div>

    <ul class="contact-list">
      <li class="contact-item item-mobile">
        <span class="contact-icon">
          <svg width="26" height="38" viewBox="0 0 26 38" fill="none" stroke="var(--icon-line)" stroke-width="2">
            <rect x="3" y="2" width="20" height="34" rx="3"/>
            <line x1="3" y1="8" x2="23" y2="8"/>
            <line x1="3" y1="29" x2="23" y2="29"/>
            <circle cx="13" cy="32.5" r="1.5"/>
          </svg>
        </span>
        <span class="contact-text">555.210.4836</span>
      </li>
      <li class="contact-item item-office">
        <span class="contact-icon">
          <svg width="38" height="34" viewBox="0 0 38 34" fill="none" stroke="var(--icon-line)" stroke-width="2">
            <rect x="2" y="4" width="9" height="26" rx="3"/>
            <rect x="13" y="6" width="23" height="22" rx="2"/>
            <g fill="var(--icon-line)" stroke="none">
              <rect x="17" y="10" width="3" height="3"/><rect x="23" y="10" width="3" height="3"/><rect x="29" y="10" width="3" height="3"/>
              <rect x="17" y="16" width="3" height="3"/><rect x="23" y="16" width="3" height="3"/><rect x="29" y="16" width="3" height="3"/>
              <rect x="17" y="22" width="3" height="3"/><rect x="23" y="22" width="3" height="3"/><rect x="29" y="22" width="3" height="3"/>
            </g>
          </svg>
        </span>
        <span class="contact-text">555.318.9072</span>
      </li>
      <li class="contact-item item-email">
        <span class="contact-icon">
          <svg width="34" height="24" viewBox="0 0 34 24" fill="none" stroke="var(--icon-line)" stroke-width="2">
            <rect x="2" y="2" width="30" height="20"/>
            <polyline points="2,2 17,14 32,2"/>
          </svg>
        </span>
        <span class="contact-text email">elan.r@vantilo.com</span>
      </li>
      <li class="contact-item item-address">
        <span class="contact-icon">
          <svg width="24" height="34" viewBox="0 0 24 34" fill="none" stroke="var(--icon-line)" stroke-width="2">
            <path d="M12 32 C6 23 3 18 3 12 A9 9 0 0 1 21 12 C21 18 18 23 12 32 Z"/>
            <circle cx="12" cy="12" r="3.5"/>
          </svg>
        </span>
        <span class="contact-text address">48 Harbor Ave. Suite 7<br>Bayport, AZ. 01568</span>
      </li>
    </ul>

    <div class="ship-artwork" role="img" aria-label="Stylised silhouette of a cruise ship sweeping across the bottom of the card"></div>
    <p class="web-address">www.vantilo.com</p>
  </main>
</body>
</html>
```